Business Card Design Project

Hi we are a media services and events agency. We have created a happy logo and would like to create a chic and sophisticated to balance out the look and feel of the namecard.

The namecard will be two sided. One side will be the logo (SUNNYBRIGHTSLANT), against two background colors - white and black.

The other side will showcase the following:

1) Two names:
Lorraine K. Fenwick
Nurhana Osman

2) designation
Co-Founder / Business Development

3) email
Lorraine.Fenwick@sunnybrightslant.example
Nurhana.Osman@sunnybrightslant.example

4) mobile number
Lorraine: +65 9000 4417
Nurhana: +65 8000 2769

5) logo of our partner:parkwanders logo enclosed. this can take up a small space on the bottom of the namecard

6) url: www.sunnybrightslant.example
We are not fussed about the color on this side. Up to designer to recommend.

Target Market(s)

Marketing, business directors, CEOs, media and advertising agencies. Audience range between 23 - 60 years of age - both male and female

Industry/Entity Type

Events

Requirements
Must have
• Our designation and company information text color should ideally not be colorful as the logo already screams color.

```html
<!DOCTYPE html>
<html lang="en">
<head>
<meta charset="utf-8">
<title>SUNNYBRIGHTSLANT – Business Cards</title>
<link rel="stylesheet" href="https://fonts.googleapis.com/css2?family=Open+Sans:wght@400;600&family=Pathway+Gothic+One&display=swap">
<style>
  :root {
    --page-bg: #eef0f2;
    --card-top: #a7a4a4;
    --card-mid: #5a5858;
    --card-bottom: #242424;
    --logo-tone: #dcdcdc;
    --tagline: #a2a2a2;
    --url: #747474;
    --name-dark: #111111;
    --detail-light: #ffffff;
    --divider-dark: #111111;
    --divider-light: #ffffff;
    --badge-blue: #29b6e8;
  }
  * { margin: 0; padding: 0; box-sizing: border-box; }
  html, body {
    width: 1200px;
    height: 1000px;
    overflow: hidden;
    background: var(--page-bg);
  }
  .canvas {
    position: relative;
    width: 1200px;
    height: 1000px;
  }
  .card {
    position: absolute;
    left: 286px;
    width: 628px;
    height: 358px;
    background: linear-gradient(180deg, var(--card-top) 0%, var(--card-mid) 45%, var(--card-bottom) 100%);
    box-shadow: 0 6px 18px rgba(0,0,0,0.18);
    overflow: hidden;
  }
  .card--front { top: 110px; }
  .card--back { top: 532px; }

  /* Front */
  .brand-name {
    position: absolute;
    top: 118px;
    width: 100%;
    text-align: center;
    font-family: "Open Sans", sans-serif;
    font-weight: 600;
    font-size: 46px;
    letter-spacing: 1px;
    color: var(--logo-tone);
  }
  .tagline {
    position: absolute;
    top: 190px;
    width: 100%;
    text-align: center;
    font-family: "Open Sans", sans-serif;
    font-size: 22px;
    letter-spacing: 1.5px;
    color: var(--tagline);
  }
  .card-url {
    position: absolute;
    width: 100%;
    text-align: center;
    font-family: "Pathway Gothic One", sans-serif;
    font-size: 24px;
    color: var(--url);
  }
  .card--front .card-url { top: 280px; font-family: "Open Sans", sans-serif; font-size: 18px; }
  .card--back .card-url { top: 292px; }

  /* Back */
  .contact {
    position: absolute;
    top: 66px;
    font-family: "Pathway Gothic One", sans-serif;
  }
  .contact--primary { left: 38px; }
  .contact--secondary { left: 336px; }
  .contact__name {
    font-size: 27px;
    line-height: 1;
    color: var(--name-dark);
  }
  .contact__role {
    margin-top: 14px;
    font-size: 27px;
    line-height: 1;
    color: var(--detail-light);
  }
  .contact__details {
    margin-top: 26px;
    padding-left: 12px;
    font-size: 25px;
    line-height: 36px;
    color: var(--detail-light);
  }
  .contact__details .email { font-size: 22px; }
  .divider {
    position: absolute;
    left: 314px;
    width: 3px;
  }
  .divider--upper { top: 58px; height: 42px; background: var(--divider-dark); }
  .divider--lower { top: 112px; height: 116px; background: var(--divider-light); }
  .partner-badge {
    position: absolute;
    top: 258px;
    width: 72px;
    height: 72px;
    background: var(--badge-blue);
  }
  .partner-badge--left { left: 30px; }
  .partner-badge--right { right: 30px; }
</style>
</head>
<body>
<main class="canvas">
  <section class="card card--front" aria-label="Card front">
    <h1 class="brand-name">SUNNYBRIGHTSLANT</h1>
    <p class="tagline">Bringing unique experiences to life</p>
    <p class="card-url">www.sunnybrightslant.example</p>
  </section>

  <section class="card card--back" aria-label="Card back">
    <div class="contact contact--primary">
      <p class="contact__name">Lorraine K. FENWICK</p>
      <p class="contact__role">Co-Founder</p>
      <p class="contact__details">+65 9000 4417<br><span class="email">Fenwick@sunnybrightslant.example</span></p>
    </div>

    <span class="divider divider--upper"></span>
    <span class="divider divider--lower"></span>

    <div class="contact contact--secondary">
      <p class="contact__name">Nurhana Osman</p>
      <p class="contact__role">Business Development</p>
      <p class="contact__details">+65 8000 2769<br><span class="email">Osman@sunnybrightslant.example</span></p>
    </div>

    <div class="partner-badge partner-badge--left" role="img" aria-label="Partner badge: parkwanders"></div>
    <p class="card-url">www.sunnybrightslant.example</p>
    <div class="partner-badge partner-badge--right" role="img" aria-label="Partner badge: parkwanders"></div>
  </section>
</main>
</body>
</html>
```